Anzeigengestaltung Zeitung für eine Zahnarztpraxis
Zielgruppe
Zahnarztpraxis, spezialisiert auf hochwertige Zahnbehandlungen.
Aufgabenstellung
Ziel soll es sein Patienten mit Zahnarztangst zu motivieren einen Ersttermin zu vereinbaren
Ganzseitige Anzeige, im Format Breite 192 mm x 290 mm.
Die Anzeige sollte sympathisch, kreativ rüberkommen um Kontaktängste abzubauen.
Es sollte ein Foto von mir als Hauptbehandler verwendet werden, es können jedoch zusätzlich auch stock Fotos dazu genommen werden. Frauen als auch Männer sollten angesprochen werden.
Kontaktangaben in der Anzeige:
Dentivera MVZ, Dr. med. dent. Lukas Brenner & Kollegen
Weidenhofer Str. 17
68519 Lampertheim
www.dentivera-beispiel.de
Tel.: 06206 5917
Email: kontakt@dentivera-beispiel.de

```html
<!DOCTYPE html>
<html lang="de">
<head>
<meta charset="utf-8">
<title>Dentivera – Anzeige Angsthase</title>
<link rel="stylesheet" href="https://fonts.googleapis.com/css2?family=Montserrat:wght@500;600;700;800&display=swap">
<style>
  :root {
    --navy-dark: #1b2446;
    --navy-light: #30507a;
    --orange: #ea6a1f;
    --white: #ffffff;
    --ink: #1e1e1e;
    --bunny-light: #f4d3a8;
    --bunny-mid: #e2a86b;
    --scrubs: #3c3a68;
    --skin: #d9a07f;
  }
  html, body {
    margin: 0;
    padding: 0;
    width: 739px;
    height: 1200px;
    overflow: hidden;
    background: #c4c3c1;
  }
  .ad {
    position: relative;
    width: 739px;
    height: 1200px;
    overflow: hidden;
    background: linear-gradient(135deg, var(--navy-light) 0%, var(--navy-dark) 55%);
    font-family: "Montserrat", sans-serif;
  }
  .ad__waves {
    position: absolute;
    inset: 0;
  }
  .brand {
    position: absolute;
    left: 57px;
    top: 80px;
    display: flex;
    align-items: center;
    gap: 16px;
    color: var(--white);
    font-weight: 600;
    font-size: 22px;
    letter-spacing: 5px;
  }
  .brand__dot {
    width: 32px;
    height: 32px;
    border-radius: 50%;
    background: var(--white);
  }
  .headline {
    position: absolute;
    left: 20px;
    top: 362px;
    width: 330px;
    margin: 0;
    text-align: center;
    font-size: 38px;
    line-height: 58px;
    font-weight: 500;
    color: var(--ink);
  }
  .headline__accent {
    color: var(--orange);
    font-weight: 800;
  }
  .photo-bunny {
    position: absolute;
    left: 345px;
    top: 210px;
    width: 370px;
    height: 545px;
    border-radius: 45% 45% 40% 40%;
    background: radial-gradient(ellipse at 50% 58%, var(--bunny-light) 0%, var(--bunny-mid) 55%, rgba(226,168,107,0) 72%);
  }
  .photo-dentist {
    position: absolute;
    left: 0;
    top: 667px;
    width: 315px;
    height: 533px;
    border-radius: 120px 120px 0 0;
    background: linear-gradient(180deg, var(--skin) 0%, #b98466 32%, var(--scrubs) 45%, #34325c 100%);
  }
  .contact {
    position: absolute;
    left: 354px;
    top: 922px;
    padding-left: 28px;
    border-left: 5px solid var(--orange);
    color: var(--white);
    font-style: normal;
    font-size: 14.5px;
    font-weight: 600;
    line-height: 21px;
  }
  .contact p { margin: 0; }
  .contact__name { font-weight: 800; }
  .contact__address { margin-top: 22px !important; }
  .contact__phone { margin-top: 40px !important; }
  .contact__web { margin-top: 20px !important; }
</style>
</head>
<body>
  <main class="ad">
    <svg class="ad__waves" viewBox="0 0 739 1200" width="739" height="1200" aria-hidden="true">
      <path fill="var(--orange)" d="M0,360 C180,200 450,80 739,46 L739,752 C600,832 430,874 300,874 C180,874 80,834 0,792 Z"/>
      <path fill="var(--white)" d="M0,405 C180,230 450,95 739,56 L739,728 C600,815 430,858 300,858 C180,858 80,820 0,778 Z"/>
    </svg>

    <div class="brand">
      <span class="brand__dot"></span>
      <span class="brand__name">Dentivera</span>
    </div>

    <h1 class="headline">
      Auch ein<br>
      <span class="headline__accent">Angsthase</span><br>
      muss mal zum<br>
      <span class="headline__accent">Zahnarzt!</span>
    </h1>

    <div class="photo-bunny" role="img" aria-label="Foto eines sitzenden hellbraunen Kaninchens mit aufgestellten Ohren"></div>
    <div class="photo-dentist" role="img" aria-label="Foto des lächelnden Zahnarztes in dunkelblauer Praxiskleidung"></div>

    <address class="contact">
      <p class="contact__name">Dentivera MVZ, Dr. med. dent.</p>
      <p class="contact__name">Lukas Brenner &amp; Kollegen</p>
      <p class="contact__address">Weidenhofer Str. 17</p>
      <p>68519 Weidenbrück</p>
      <p class="contact__phone">Tel.: 04321 5917</p>
      <p>E-Mail: kontakt@dentivera-beispiel.de</p>
      <p class="contact__web">www.dentivera-beispiel.de</p>
    </address>
  </main>
</body>
</html>
```